Poster to promote Global Critter Care Fest

Hi Designers,

Animal lovers all over the world are grateful for the work of vets.

To recognize all their efforts, Global Critter Care Fest takes place globally on April 30. This year's theme is 'Continuing education with a one health focus'.

It's about working alongside the human health sector to tackle animal disease and food safety. Read more here: http://www.kalvora.int/for-the-media/press-releases/detail/article/global-critter-care-fest-award-2016/

We want you to design a poster to promote the day, and the key message.

The poster must feature:
- the words 'Global Critter Care Fest'
- the date 'April 30, 2016'
- the theme 'Continuing education with a one health focus

You can choose any imagery and colors you feel will be engaging for the audience and will reflect the industry and messages.

Think animal, vets, pets, caring, health.

Looking forward to seeing your ideas.

Thanks

Pixelhive

Veterinary

• - the words 'Global Critter Care Fest'
• - the date 'April 30, 2016'
• - the theme 'Continuing education with a one health focus

```html
<!DOCTYPE html>
<html lang="en">
<head>
<meta charset="utf-8">
<title>Global Critter Care Fest – April 30, 2016</title>
<link rel="stylesheet" href="https://fonts.googleapis.com/css2?family=Questrial&family=Arimo:wght@700&display=swap">
<style>
  :root {
    --backdrop: #d4d4d4;
    --teal-deep: #1f8a78;
    --teal-mid: #3aa693;
    --teal-light: #6cc2b0;
    --silver-hi: #ffffff;
    --silver-mid: #d9dcdc;
    --silver-lo: #9ea3a3;
    --photo-warm: #c9a17a;
    --photo-cool: #2f6f66;
    --text-shadow: rgba(0, 40, 34, 0.55);
  }
  * { margin: 0; padding: 0; box-sizing: border-box; }
  html, body {
    width: 800px; height: 1200px; overflow: hidden;
    background: var(--backdrop);
  }
  .poster {
    position: absolute; left: 58px; top: 105px;
    width: 687px; height: 975px; overflow: hidden;
    background:
      radial-gradient(ellipse at 80% 30%, var(--teal-light) 0%, transparent 45%),
      radial-gradient(ellipse at 15% 70%, var(--teal-deep) 0%, transparent 55%),
      radial-gradient(ellipse at 85% 85%, var(--teal-light) 0%, transparent 40%),
      linear-gradient(160deg, var(--teal-mid), var(--teal-deep) 60%, var(--teal-mid));
  }
  .portrait-frame {
    position: absolute; left: 64px; top: 40px;
    width: 560px; height: 562px;
  }
  .headline {
    position: absolute; left: 0; width: 100%;
    text-align: center; text-transform: uppercase;
    font-family: "Questrial", "Century Gothic", sans-serif;
    color: var(--silver-mid);
    background: linear-gradient(180deg, var(--silver-hi) 0%, var(--silver-mid) 55%, var(--silver-lo) 100%);
    -webkit-background-clip: text; background-clip: text;
    -webkit-text-fill-color: transparent;
    filter: drop-shadow(2px 3px 3px var(--text-shadow));
    line-height: 1;
  }
  .headline--main { top: 618px; font-size: 112px; letter-spacing: 2px; }
  .headline--sub { top: 733px; font-size: 46px; letter-spacing: 1px; }
  .event-date {
    position: absolute; left: 0; top: 792px; width: 100%;
    text-align: center;
    font-family: "Arimo", Arial, sans-serif; font-weight: 700;
    font-size: 62px; line-height: 1;
    color: var(--silver-hi);
    filter: drop-shadow(2px 3px 3px var(--text-shadow));
  }
  .theme {
    position: absolute; left: 0; top: 868px; width: 100%;
    text-align: center; text-transform: uppercase;
    font-family: "Questrial", "Century Gothic", sans-serif;
    font-size: 33px; line-height: 37px; letter-spacing: 0.5px;
    color: var(--silver-hi);
    filter: drop-shadow(1px 2px 2px var(--text-shadow));
  }
</style>
</head>
<body>
  <main class="poster">
    <svg class="portrait-frame" viewBox="0 0 560 562" width="560" height="562">
      <defs>
        <linearGradient id="ring-silver" x1="0" y1="0" x2="1" y2="1">
          <stop offset="0" stop-color="#ffffff"/>
          <stop offset="0.5" stop-color="#c9cccc"/>
          <stop offset="1" stop-color="#f4f4f4"/>
        </linearGradient>
        <linearGradient id="photo-tones" x1="0" y1="0" x2="1" y2="0">
          <stop offset="0" stop-color="#2f6f66"/>
          <stop offset="0.45" stop-color="#a9b2ad"/>
          <stop offset="1" stop-color="#c9a17a"/>
        </linearGradient>
      </defs>
      <ellipse cx="280" cy="281" rx="278" ry="279" fill="url(#ring-silver)"/>
      <ellipse cx="280" cy="281" rx="256" ry="258" fill="url(#photo-tones)"
               role="img" aria-label="Photo: a veterinarian in green scrubs kneeling and gently examining the paw of a tan and white dog in a clinic"/>
    </svg>

    <h1 class="headline headline--main">Global</h1>
    <h2 class="headline headline--sub">Critter Care Fest</h2>
    <p class="event-date">April 30, 2016</p>
    <p class="theme">Continuing education<br>with a one health focus</p>
  </main>
</body>
</html>
```